Wordpress Design for a Digital Management Consulting Business

I need a simple Wordpress Design and someone to set it up for a new boutique management consulting business called Tidewell Advisory that specialises in providing strategic advice to help grow digital businesses. It covers business strategy, marketing strategy, digital strategy, web product development, marketing campaigns, social, search, etc. From strategy to implementation.

URL is: tidewelladvisory.com.au

My professional background is here: au.examplenet.com/in/norabellweather

Competitors: other boutique digital/marketing management consulting businesses in Australia

The logos, colours and fonts are attached.

I would like the site to convey a business that is Smart/intelligent, Contemporary, Progressive, Digital, Energetic, Friendly.

The objective of the site is to educate visitors about what Tidewell Advisory does and encourage them to contact me for more information. It will be very light on content.

Target Market(s)

CEOs/Managing Directors, General Managers, Marketing Directors

Industry/Entity Type

Management Consulting

Font styles to use
Sans Serif

Colors
e34197
5c5c5c
000000

Requirements
Must have
• Site design requirements:
• Choose an appropriate Wordpress template, set it up for me and let me be able to edit it ongoing.
• It should use lots of images - these can be inspirational and not necessarily tied directly to the work
• Pink should feature, but not be the dominant colour.
• Site structure should be:
• 1. Home page - image led with horizontal navigation. Text beneath and images to describe the services.
• 2. About page - with space to write text and insert a picture of the Director
• 3. Services - with space to highlight services either as a list or graphically with text
• 4. Contact page - with space to write text and add email links, etc.
• Should have horizontal navigation
• It should have the flexibility to add another page
Nice to have
• Use the tree icon somehow in the design - consider in the background enlarged
• Use pink, grey, black from logo. Can introduce another complimentary colour if necessary.
• Can introduce another complimentary font to go with the logo font.
Should not have
• Use cliched business images and icons, eg. business suits, hand shakes, business men, business ties.

```html
<!DOCTYPE html>
<html lang="en">
<head>
<meta charset="utf-8">
<title>Tidewell Advisory</title>
<link href="https://fonts.googleapis.com/css2?family=Open+Sans:wght@400;600;700&display=swap" rel="stylesheet">
<style>
:root{
  --pink:#e34197;
  --grey:#5c5c5c;
  --black:#000000;
  --ink:#333333;
  --muted:#8a8a8a;
  --light:#f4f4f4;
  --navy:#0d1628;
  --bar:#3a3a3a;
  --white:#ffffff;
}
*{box-sizing:border-box;margin:0;padding:0}
html,body{width:1200px;height:2272px;overflow:hidden}
body{font-family:"Open Sans",Arial,sans-serif;color:var(--ink);background:var(--white);position:relative}
section,header,footer{position:absolute;left:0;width:1200px}

/* Hero */
.hero{top:0;height:660px;overflow:hidden}
.hero-photo{position:absolute;inset:0;background:
  radial-gradient(ellipse 500px 260px at 780px 420px,rgba(214,120,40,.55),transparent 70%),
  radial-gradient(ellipse 700px 300px at 900px 620px,rgba(150,70,30,.45),transparent 70%),
  linear-gradient(180deg,#1b1f26 0%,#262a30 45%,#3a2a22 80%,#1c1612 100%)}
.topbar{position:absolute;top:0;left:0;width:1200px;height:130px;display:flex;align-items:center;justify-content:space-between;padding:0 60px 0 68px}
.brand{display:flex;align-items:center;gap:10px;color:var(--white);font-size:26px;font-weight:600;letter-spacing:.5px}
.brand-dot{width:22px;height:22px;border-radius:50%;background:var(--pink)}
.nav{display:flex;gap:46px;list-style:none}
.nav li{color:var(--white);font-size:12px;font-weight:600;letter-spacing:.5px}
.nav li.active{color:var(--pink)}
.hero-copy{position:absolute;left:0;top:372px;padding-left:0}
.hero-title{color:var(--white);font-size:52px;font-weight:400;line-height:1;padding-left:0;letter-spacing:1px}
.hero-sub{margin-top:10px;color:var(--white);font-size:24px;font-weight:400}
.hero-text{margin-top:12px;width:560px;color:#dcdcdc;font-size:14px;line-height:22px}
.btn{display:inline-block;margin-top:40px;background:var(--pink);color:var(--white);font-size:12px;font-weight:700;letter-spacing:.5px;padding:13px 26px}

/* Welcome */
.welcome{top:660px;height:240px;text-align:center}
.section-title{font-size:28px;font-weight:700;color:var(--ink);letter-spacing:.3px}
.welcome .section-title{margin-top:58px}
.lead{width:860px;margin:22px auto 0;font-size:12px;line-height:22px;color:var(--muted)}

/* Services */
.services{top:900px;height:470px;text-align:center}
.services .section-title{margin-top:0}
.cards{position:absolute;top:72px;left:100px;width:1000px;display:flex;gap:30px;text-align:left}
.card{width:313px}
.card-photo{height:185px}
.card h3{margin-top:22px;font-size:13px;font-weight:700;color:var(--ink)}
.card p{margin-top:8px;font-size:12px;line-height:20px;color:var(--muted)}
.photo-keys{background:linear-gradient(135deg,#dfe6ec 0%,#8aa6bd 40%,#2f8fc6 60%,#cfd8df 100%)}
.photo-towers{background:linear-gradient(180deg,#e9edf1 0%,#b9c2cb 45%,#6d7884 100%)}
.photo-figures{background:linear-gradient(180deg,#f5f5f5 0%,#cfcfcf 60%,#a9a9a9 100%)}
.dots{position:absolute;left:0;width:100%;display:flex;justify-content:center;gap:8px}
.dots span{width:7px;height:7px;border-radius:50%;background:#cfcfcf}
.dots span.on{background:var(--pink)}
.services .dots{top:398px}

/* Strategy */
.strategy{top:1370px;height:510px;overflow:hidden;color:var(--white);text-align:center}
.strategy-photo{position:absolute;inset:0;background:
  radial-gradient(ellipse 900px 260px at 600px 560px,rgba(60,120,200,.55),transparent 70%),
  linear-gradient(180deg,#050a14 0%,#0b1730 60%,#13284d 100%)}
.strategy .section-title{position:relative;margin-top:70px;color:var(--white)}
.strategy .lead{position:relative;color:#c7cbd3}
.pillars{position:absolute;top:262px;left:100px;width:1000px;display:flex;gap:30px;text-align:left}
.pillar{width:227px}
.pillar svg{display:block}
.pillar h4{margin-top:12px;font-size:11px;font-weight:700;color:var(--white);letter-spacing:.3px}
.pillar .rule{width:40px;height:1px;background:#7a8294;margin:6px 0 10px}
.pillar p{font-size:11px;line-height:19px;color:#c7cbd3}
.strategy .dots{top:458px}

/* Footer */
.site-footer{top:1880px;height:320px;background:var(--white)}
.fcols{position:absolute;top:28px;left:100px;width:1000px;display:flex;gap:40px}
.fcol{width:220px}
.fcol h5{font-size:11px;font-weight:700;color:var(--pink);letter-spacing:.4px}
.fcol ul{list-style:none;margin-top:14px}
.fcol li{font-size:11px;line-height:20px;color:var(--muted)}
.post{margin-bottom:14px}
.post p{font-size:11px;line-height:18px;color:var(--muted)}
.post span{font-size:10px;color:var(--pink)}
.social{display:flex;gap:6px;margin-top:12px}
.social span{width:20px;height:20px;background:var(--pink)}
.bottombar{position:absolute;top:2200px;left:0;width:1200px;height:72px;background:var(--bar);display:flex;align-items:center;justify-content:space-between;padding:0 60px 0 100px}
.bottombar .brand{font-size:20px;color:#cfcfcf}
.bottombar .brand-dot{width:16px;height:16px}
.legal{display:flex;gap:28px;font-size:10px;color:#b5b5b5}
</style>
</head>
<body>

<header class="hero">
  <div class="hero-photo" role="img" aria-label="Night photograph of a suspension bridge lit in warm orange over a city bay"></div>
  <div class="topbar">
    <div class="brand"><span class="brand-dot"></span>Tidewell Advisory</div>
    <ul class="nav">
      <li class="active">HOME</li><li>ABOUT US</li><li>STRATEGY</li><li>FEATURES</li><li>TESTIMONIALS</li><li>CONTACT US</li>
    </ul>
  </div>
  <div class="hero-copy" style="left:68px">
    <h1 class="hero-title">WE ARE A</h1>
    <p class="hero-sub">new boutique management consulting business</p>
    <p class="hero-text">We cover business strategy, marketing strategy, digital strategy, web product development, marketing campaigns, social, search etc.</p>
    <span class="btn">READ MORE INFO</span>
  </div>
</header>

<section class="welcome">
  <h2 class="section-title">WELCOME TO TIDEWELL ADVISORY</h2>
  <p class="lead">Lorem ipsum is simply dummy text of the printing and typesetting industry. Lorem Ipsum has been the industry's standard dummy text ever since the 1500s, when an unknown printer took a galley of type and scrambled it to make a type specimen book. It has survived not only five centuries but also the leap into electronic typesetting.</p>
</section>

<section class="services">
  <h2 class="section-title">FEATURES OF SERVICES</h2>
  <div class="cards">
    <article class="card">
      <div class="card-photo photo-keys" role="img" aria-label="Close-up of a keyboard with a highlighted blue key"></div>
      <h3>LOREM IPSUM IS SIMPLY DUMMY</h3>
      <p>Lorem ipsum is simply dummy text of the printing and typesetting industry. Lorem Ipsum has been the industry's standard dummy text.</p>
    </article>
    <article class="card">
      <div class="card-photo photo-towers" role="img" aria-label="Glass office towers seen against a pale sky"></div>
      <h3>LOREM IPSUM IS SIMPLY DUMMY</h3>
      <p>Lorem ipsum is simply dummy text of the printing and typesetting industry. Lorem Ipsum has been the industry's standard dummy text.</p>
    </article>
    <article class="card">
      <div class="card-photo photo-figures" role="img" aria-label="Grey three-dimensional figures standing in a group"></div>
      <h3>LOREM IPSUM IS SIMPLY DUMMY</h3>
      <p>Lorem ipsum is simply dummy text of the printing and typesetting industry. Lorem Ipsum has been the industry's standard dummy text.</p>
    </article>
  </div>
  <div class="dots"><span class="on"></span><span></span><span></span></div>
</section>

<section class="strategy">
  <div class="strategy-photo" role="img" aria-label="Earth from orbit at night with a glowing blue horizon"></div>
  <h2 class="section-title">STRATEGY TO IMPLEMENTATION</h2>
  <p class="lead">Lorem ipsum is simply dummy text of the printing and typesetting industry. Lorem Ipsum has been the industry's standard dummy text ever since the 1500s, when an unknown printer took a galley of type and scrambled it to make a type specimen book. It has survived not only five centuries but also the leap into electronic typesetting.</p>
  <div class="pillars">
    <div class="pillar">
      <svg width="26" height="22" viewBox="0 0 26 22"><rect x="1" y="6" width="24" height="15" rx="2" fill="#e34197"/><rect x="8" y="1" width="10" height="6" rx="1" fill="none" stroke="#e34197" stroke-width="2"/></svg>
      <h4>BUSINESS STRATEGY</h4><div class="rule"></div>
      <p>Lorem ipsum is simply dummy text of the printing and typesetting industry, been the industry.</p>
    </div>
    <div class="pillar">
      <svg width="26" height="22" viewBox="0 0 26 22"><path d="M2 8h6l12-6v18L8 14H2z" fill="#e34197"/><rect x="5" y="14" width="4" height="7" fill="#e34197"/></svg>
      <h4>MARKETING STRATEGY</h4><div class="rule"></div>
      <p>Lorem ipsum is simply dummy text of the printing and typesetting industry, been the industry.</p>
    </div>
    <div class="pillar">
      <svg width="26" height="22" viewBox="0 0 26 22"><rect x="1" y="1" width="24" height="15" rx="1" fill="#e34197"/><rect x="10" y="16" width="6" height="3" fill="#e34197"/><rect x="6" y="19" width="14" height="2" fill="#e34197"/></svg>
      <h4>DIGITAL STRATEGY</h4><div class="rule"></div>
      <p>Lorem ipsum is simply dummy text of the printing and typesetting industry, been the industry.</p>
    </div>
    <div class="pillar">
      <svg width="26" height="22" viewBox="0 0 26 22"><circle cx="10" cy="12" r="6" fill="none" stroke="#e34197" stroke-width="4"/><circle cx="20" cy="5" r="3" fill="none" stroke="#e34197" stroke-width="2.5"/></svg>
      <h4>WEB PRODUCT DEVELOPMENT</h4><div class="rule"></div>
      <p>Lorem ipsum is simply dummy text of the printing and typesetting industry, been the industry.</p>
    </div>
  </div>
  <div class="dots"><span></span><span class="on"></span><span></span></div>
</section>

<footer class="site-footer">
  <div class="fcols">
    <div class="fcol">
      <h5>RECENT POSTS</h5>
      <ul>
        <li class="post"><p>Lorem ipsum is simply dummy text of the printing</p><span>Posted on 21 March 2015</span></li>
        <li class="post"><p>Lorem ipsum is simply dummy text of the printing</p><span>Posted on 14 March 2015</span></li>
        <li class="post"><p>Lorem ipsum is simply dummy text of the printing</p><span>Posted on 02 March 2015</span></li>
      </ul>
    </div>
    <div class="fcol">
      <h5>WELCOME</h5>
      <ul><li>Home</li><li>About Us</li><li>Strategy</li><li>Features</li><li>Testimonials</li><li>Contact Us</li></ul>
    </div>
    <div class="fcol">
      <h5>STRATEGY</h5>
      <ul><li>Business strategy</li><li>Marketing strategy</li><li>Digital strategy</li><li>Web product development</li><li>Marketing campaigns</li><li>Social</li><li>Search</li></ul>
    </div>
    <div class="fcol">
      <h5>CONTACT US</h5>
      <ul><li>120 Harbour Lane, City Centre</li><li>Victoria 3000</li><li>(03) 5550 0142</li><li>info@tidewelladvisory.com.au</li></ul>
      <div class="social"><span></span><span></span><span></span><span></span><span></span></div>
    </div>
  </div>
</footer>

<div class="bottombar">
  <div class="brand"><span class="brand-dot"></span>Tidewell Advisory</div>
  <div class="legal"><span>© 2015 Tidewell Advisory. All Rights Reserved.</span><span>Privacy Policy</span><span>Accessibility</span><span>Contact</span><span>Sitemap</span><span>Top</span></div>
</div>

</body>
</html>
```